Need a sleek, professional business card design for a Web Development business

I need a unique business card designed for a web development company. It is also the parent company for any ventures I do, such as my ClipWave channel, startup ideas I have, etc. I am the single member of "Bright Harbor Code LLC." I will attach my basic logo here, so you will see the current color scheme and have the asset available. Thank you!

Target Market(s)

Startups, SMB's, Professionals

Industry/Entity Type

Business

Font styles to use
Other font styles liked:
• Lovello for headings is what I use, but not necessary.

Colors

Designer to choose colors to be used in the design.

Requirements
Nice to have
• Sleek is the word. Professional, modern, dark.
Should not have
• Any work from someone else's design. Lacking originality.

```html
<!DOCTYPE html>
<html lang="en">
<head>
<meta charset="utf-8">
<title>Bright Harbor Code LLC — Business Card</title>
<link href="https://fonts.googleapis.com/css2?family=Ubuntu:wght@400;500&family=Ubuntu+Condensed&display=swap" rel="stylesheet">
<style>
  :root {
    --page: #f2f2f2;
    --ink: #000000;
    --paper: #ffffff;
    --orange-light: #f7941d;
    --orange-deep: #ee5a24;
    --icon-grey: #a7a9ac;
    --muted: #6d6e71;
    --faint: #2a2a2a;
    --text-dark: #1a1a1a;
  }
  * { margin: 0; padding: 0; box-sizing: border-box; }
  html, body {
    width: 1200px; height: 1200px; overflow: hidden;
    background: var(--page);
  }
  .card {
    position: absolute; left: 100px; top: 310px;
    width: 1000px; height: 580px;
    background: var(--paper);
    box-shadow: 0 18px 40px rgba(0,0,0,0.18);
    overflow: hidden;
    font-family: "Ubuntu", sans-serif;
  }
  .card-base { position: absolute; inset: 0; }
  .brand-mark {
    position: absolute; left: 40px; top: 110px;
    width: 150px; height: 150px;
    border: 3px solid var(--paper); border-radius: 8px;
  }
  .brand-block { position: absolute; left: 222px; top: 150px; width: 410px; }
  .brand-name {
    color: var(--paper); font-size: 36px; font-weight: 400;
    letter-spacing: 0.3px; white-space: nowrap;
    padding-bottom: 6px; border-bottom: 1px solid var(--muted);
  }
  .brand-tagline {
    color: var(--paper); font-family: "Ubuntu Condensed", sans-serif;
    font-size: 18px; margin-top: 6px; white-space: nowrap;
  }
  .brand-tagline .dim { color: var(--muted); }
  .faint-mark {
    position: absolute; left: 660px; top: 150px;
    width: 115px; height: 115px;
    border: 2px solid var(--faint); border-radius: 6px;
  }
  .person, .address {
    position: absolute; right: 36px; width: 180px; text-align: right;
    color: var(--paper); font-family: "Ubuntu Condensed", sans-serif;
    white-space: nowrap;
  }
  .person { top: 158px; }
  .person-name { font-size: 23px; display: flex; align-items: center; justify-content: flex-end; gap: 8px; }
  .person-role { font-size: 22px; margin-top: 2px; }
  .address { top: 300px; }
  .address-label {
    font-size: 22px; display: flex; align-items: center; justify-content: flex-end; gap: 8px;
    padding-bottom: 4px; border-bottom: 1px solid var(--muted);
  }
  .address-line { font-size: 22px; margin-top: 8px; }
  .contacts {
    position: absolute; left: 130px; right: 40px; top: 490px;
    display: flex; align-items: center; justify-content: flex-end; gap: 32px;
    font-family: "Ubuntu Condensed", sans-serif; font-size: 26px; color: var(--text-dark);
  }
  .contact { display: flex; align-items: center; gap: 12px; white-space: nowrap; }
</style>
</head>
<body>
  <div class="card">
    <svg class="card-base" width="1000" height="580" viewBox="0 0 1000 580" aria-hidden="true">
      <defs>
        <linearGradient id="band" x1="0" y1="0" x2="1" y2="0">
          <stop offset="0" stop-color="var(--orange-light)"/>
          <stop offset="0.45" stop-color="var(--orange-deep)"/>
          <stop offset="0.55" stop-color="var(--orange-light)"/>
          <stop offset="1" stop-color="var(--orange-deep)"/>
        </linearGradient>
      </defs>
      <rect x="0" y="0" width="1000" height="430" fill="var(--ink)"/>
      <polygon points="0,425 450,425 500,395 550,425 1000,425 1000,465 550,465 500,440 450,465 0,465" fill="url(#band)"/>
      <polygon points="450,425 500,395 500,440 450,465" fill="#000" opacity="0.12"/>
    </svg>

    <div class="brand-mark" aria-hidden="true"></div>
    <div class="brand-block">
      <div class="brand-name">Bright Harbor Code LLC</div>
      <div class="brand-tagline">Sleek is the word. Professional, modern, <span class="dim">dark.</span></div>
    </div>

    <div class="faint-mark" aria-hidden="true"></div>

    <div class="person">
      <div class="person-name">John DOE
        <svg width="26" height="26" viewBox="0 0 24 24" aria-hidden="true"><circle cx="12" cy="7" r="5" fill="#fff"/><path d="M2 23c0-6 4.5-9 10-9s10 3 10 9z" fill="#fff"/></svg>
      </div>
      <div class="person-role">Web Developer</div>
    </div>

    <div class="address">
      <div class="address-label">Address
        <svg width="28" height="26" viewBox="0 0 24 22" aria-hidden="true"><path d="M12 2 1 11h3v10h6v-6h4v6h6V11h3z" fill="none" stroke="#fff" stroke-width="2" stroke-linejoin="round"/></svg>
      </div>
      <div class="address-line">Street</div>
    </div>

    <div class="contacts">
      <div class="contact">
        <svg width="24" height="42" viewBox="0 0 28 48" aria-hidden="true"><rect x="2" y="8" width="24" height="38" rx="5" fill="var(--icon-grey)"/><rect x="5" y="1" width="4" height="9" rx="2" fill="var(--icon-grey)"/><rect x="7" y="14" width="14" height="12" fill="#fff"/><circle cx="14" cy="37" r="3" fill="#fff"/></svg>
        <span>123456790</span>
      </div>
      <div class="contact">
        <svg width="56" height="40" viewBox="0 0 70 50" aria-hidden="true"><rect x="3" y="3" width="64" height="44" fill="none" stroke="var(--icon-grey)" stroke-width="5"/><path d="M3 3 35 28 67 3" fill="none" stroke="var(--icon-grey)" stroke-width="5"/></svg>
        <span>info@example.com</span>
      </div>
      <div class="contact">
        <svg width="42" height="42" viewBox="0 0 50 50" aria-hidden="true"><g fill="none" stroke="var(--icon-grey)" stroke-width="3"><circle cx="22" cy="22" r="19"/><ellipse cx="22" cy="22" rx="8" ry="19"/><path d="M3 22h38M6 12h32M6 32h32"/></g><path d="M30 28 46 36 39 38 45 46 41 48 36 40 31 45z" fill="var(--icon-grey)"/></svg>
        <span>www.example.com</span>
      </div>
    </div>
  </div>
</body>
</html>
```